W.I.Q 'Wadi Ibn Qutub' for General Transportation

this company is a Iraqi based company.
It provides a number of logistics activities such as;
Overland Transportation
High and heavy logistics
Customs clearance
warehousing
Automotive logistics
The company has been registered since 2009.
If you have any other questions please feel free to ask.
Target Market(s)
Automotive
White goods
All Trading sectors
Industry/Entity Type
Automotive

```html
<!DOCTYPE html>
<html lang="en">
<head>
<meta charset="utf-8">
<title>Wadi Ibn Qutub Transportation</title>
<link href="https://fonts.googleapis.com/css2?family=Ubuntu:wght@400;500;700&family=Open+Sans:wght@400;600&display=swap" rel="stylesheet">
<style>
:root{
  --brand:#0d3f7f;
  --brand-dark:#071b3a;
  --heading:#2e4f7a;
  --text:#555b63;
  --muted:#8a8f96;
  --footer:#3b3b3b;
  --footer-bottom:#2a2a2a;
  --footer-text:#b8b8b8;
  --link:#4a9be8;
}
*{margin:0;padding:0;box-sizing:border-box}
html,body{width:1024px;height:1200px;overflow:hidden}
body{position:relative;background:#fbfcfd;font-family:'Ubuntu',sans-serif;color:var(--text)}
.abs{position:absolute}

.site-header{position:absolute;left:0;top:0;width:1024px;height:61px;background:linear-gradient(#fff,#eef0f2);border-bottom:1px solid #d8dbdf;z-index:2}
.brand{position:absolute;left:135px;top:14px;display:flex;align-items:center;gap:12px}
.brand-mark{font-family:'Ubuntu',sans-serif;font-weight:700;font-size:30px;color:var(--brand);letter-spacing:1px}
.brand-name{font-size:15px;line-height:17px;color:var(--brand);font-weight:400}
.brand-name span{display:block;color:#8d9196}
.main-nav a{position:absolute;top:27px;font-size:12px;color:#333;text-decoration:none}
.main-nav a.active{color:var(--brand)}
.nav-indicator{position:absolute;left:464px;top:0;width:35px;height:3px;background:var(--brand)}
.call{position:absolute;left:776px;top:22px;display:flex;gap:10px}
.call small{display:block;font-size:9px;color:#8a8f96;letter-spacing:.3px}
.call strong{display:block;font-size:11.5px;color:var(--brand);font-weight:700}

.hero{position:absolute;left:0;top:61px;width:1024px;height:527px;background:
  radial-gradient(ellipse 300px 260px at 220px 300px,#eef1f5 0%,#c3ccd7 55%,transparent 80%),
  linear-gradient(170deg,#dfe4ea 0%,#a9b6c6 30%,#5b6e88 60%,#2a3c58 100%)}
.hero-caption{position:absolute;left:542px;top:240px;width:482px;height:130px;background:linear-gradient(90deg,rgba(8,30,72,.95),rgba(6,18,42,.9));color:#fff;padding:22px 0 0 39px}
.hero-caption h1{font-weight:400;font-size:26px;line-height:34px}
.hero-caption p{font-size:14px;margin-top:6px;margin-left:3px}

.band{position:absolute;left:0;top:588px;width:1024px;height:200px;background:linear-gradient(#dde1e5,#fbfcfd)}

.service-card{position:absolute;top:519px;width:177px;height:233px;background:#fff;border-top:5px solid #9a9ea3;box-shadow:0 1px 3px rgba(0,0,0,.15)}
.service-card h3{text-align:center;font-size:11.5px;font-weight:500;color:var(--heading);margin-top:23px}
.service-card .photo{position:absolute;left:14px;top:47px;width:149px;height:78px}
.service-card p{position:absolute;left:14px;top:145px;width:152px;font-family:'Open Sans',sans-serif;font-size:7.5px;line-height:11px;color:#666}
.service-card a{position:absolute;left:14px;top:197px;font-size:8px;font-weight:700;color:var(--heading)}

.section-title{position:absolute;top:824px;font-size:14.5px;font-weight:500;color:var(--heading)}
.welcome-photo{position:absolute;left:136px;top:859px;width:112px;height:87px;background:linear-gradient(135deg,#3f5f8c,#c6a068 50%,#e6e2dc)}
.welcome-text{position:absolute;left:266px;top:855px;width:240px;font-size:10.5px;line-height:16px;color:#555}
.why-list{position:absolute;left:529px;top:859px;list-style:none}
.why-list li{display:flex;align-items:center;height:27.3px;font-size:10.5px;color:#555}
.why-list svg{margin-right:11px}

.site-footer{position:absolute;left:0;top:1019px;width:1024px;height:147px;background:linear-gradient(#333,var(--footer) 10%);border-top:2px solid #555}
.footer-mark{position:absolute;left:169px;top:1070px;font-size:32px;font-weight:700;color:#7b7b7b;letter-spacing:1px}
.footer-col{position:absolute;top:1045px}
.footer-col h4{font-size:12px;font-weight:500;color:#fff;margin-bottom:9px}
.footer-col ul{list-style:none}
.footer-col li{font-family:'Open Sans',sans-serif;font-size:8.5px;color:var(--footer-text);height:19px;display:flex;align-items:center;gap:6px}
.footer-col li.hover{color:var(--link)}
.contact-col li{height:24px;gap:10px}
.socials{display:flex;gap:9px;margin-top:2px}
.socials span{width:27px;height:27px;border-radius:2px;box-shadow:0 1px 2px rgba(0,0,0,.5)}
.footer-bottom{position:absolute;left:0;top:1166px;width:1024px;height:34px;background:var(--footer-bottom);font-family:'Open Sans',sans-serif;font-size:8.5px;color:#a9a9a9}
.footer-bottom .copy{position:absolute;left:134px;top:11px}
.footer-bottom .legal{position:absolute;right:130px;top:11px}
</style>
</head>
<body>

<header class="site-header">
  <div class="brand">
    <span class="brand-mark">W.I.Q</span>
    <span class="brand-name">Wadi Ibn Qutub<span>Transportation</span></span>
  </div>
  <nav class="main-nav">
    <div class="nav-indicator"></div>
    <a class="active" style="left:468px">Home</a>
    <a style="left:534px">Services</a>
    <a style="left:617px">About</a>
    <a style="left:685px">Contact</a>
  </nav>
  <div class="call">
    <svg width="19" height="19" viewBox="0 0 19 19"><rect width="19" height="19" rx="3" fill="#0d3f7f"/><path d="M6 4.5l2 2.5-1.2 1.3c.6 1.4 1.6 2.4 3 3L11 10l2.5 2-1 2c-4 .2-7.7-3.5-7.5-7.5z" fill="#fff"/></svg>
    <div><small>CALL US TODAY</small><strong>1800.555.0142</strong></div>
  </div>
</header>

<section class="hero" role="img" aria-label="White delivery truck driving at speed, motion-blurred sky behind">
  <div class="hero-caption">
    <h1>We provide the highest<br>quality of service you need.</h1>
    <p>Lorem ipsum dolor sit amet, consectetur adipisicing</p>
  </div>
</section>
<div class="band"></div>

<article class="service-card" style="left:135px">
  <h3>Overland Transportation</h3>
  <div class="photo" role="img" aria-label="Truck trailer on an open highway" style="background:linear-gradient(#5d84b8,#c9d5e3 55%,#6b6a5e 75%,#8c7b58)"></div>
  <p>Lorem ipsum dolor sit amet, consectetur adipisicing elit, sed do eiusmod tempor incididunt ut labore .</p>
  <a>READ MORE</a>
</article>
<article class="service-card" style="left:327px">
  <h3>High and Heavy Logistics</h3>
  <div class="photo" role="img" aria-label="Worker in orange safety gear beside shipping containers" style="background:linear-gradient(90deg,#2c4d7a,#4a6788 45%,#c96a3a 55%,#bfc8d4 70%,#d7dde5)"></div>
  <p>Lorem ipsum dolor sit amet, consectetur adipisicing elit, sed do eiusmod tempor incididunt ut labore .</p>
  <a>READ MORE</a>
</article>
<article class="service-card" style="left:519px">
  <h3>Customs Clearance</h3>
  <div class="photo" role="img" aria-label="Empty warehouse hall with tall windows" style="background:linear-gradient(#4a3b22,#b8923f 50%,#6b5630)"></div>
  <p>Lorem ipsum dolor sit amet, consectetur adipisicing elit, sed do eiusmod tempor incididunt ut labore .</p>
  <a>READ MORE</a>
</article>
<article class="service-card" style="left:711px">
  <h3>Automotive Logistics</h3>
  <div class="photo" role="img" aria-label="Workers loading cardboard boxes into a truck" style="background:linear-gradient(90deg,#3a3a3a,#d0d0d0 25%,#2f8d80 45%,#c79a6a 70%,#d8b58a)"></div>
  <p>Lorem ipsum dolor sit amet, consectetur adipisicing elit, sed do eiusmod tempor incididunt ut labore .</p>
  <a>READ MORE</a>
</article>

<h2 class="section-title" style="left:136px">Welcome to Wadi Ibn Qutub Transporation</h2>
<div class="welcome-photo" role="img" aria-label="Forklift in a warehouse with stacked shelves"></div>
<p class="welcome-text">It is a long established fact that a reader will be distracted by the readable content of a page when looking at its layout. The point of using Lorem Ipsum is that it has a more-or-less normal distribution of letters, as opposed to using 'Content here, content here', making it look like.</p>

<h2 class="section-title" style="left:527px">Why Choose Us?</h2>
<ul class="why-list">
  <li><svg width="14" height="14"><circle cx="7" cy="7" r="7" fill="#8e9298"/><path d="M6 4l3 3-3 3" stroke="#fff" stroke-width="1.5" fill="none"/></svg>Cras rutrum leo at odio volutpat id blandit fugiats ipsum ornare.</li>
  <li><svg width="14" height="14"><circle cx="7" cy="7" r="7" fill="#8e9298"/><path d="M6 4l3 3-3 3" stroke="#fff" stroke-width="1.5" fill="none"/></svg>Donec fermentum porttitor nunc, sit amet gravida est porttitor vel.</li>
  <li><svg width="14" height="14"><circle cx="7" cy="7" r="7" fill="#8e9298"/><path d="M6 4l3 3-3 3" stroke="#fff" stroke-width="1.5" fill="none"/></svg>Maecenas quis nisi in uctus adipiscing sed vehicula tellus amet dolore.</li>
  <li><svg width="14" height="14"><circle cx="7" cy="7" r="7" fill="#8e9298"/><path d="M6 4l3 3-3 3" stroke="#fff" stroke-width="1.5" fill="none"/></svg>Aenean faucibus sapien a odio varius aliquet voluptas sadips..</li>
</ul>

<footer>
  <div class="site-footer"></div>
  <div class="footer-mark">W.I.Q</div>
  <div class="footer-col" style="left:329px">
    <h4>Navigation</h4>
    <ul><li>▸ Home</li><li>▸ About</li><li>▸ Services</li><li>▸ Contact</li></ul>
  </div>
  <div class="footer-col" style="left:457px">
    <h4>Services</h4>
    <ul><li class="hover">▸ Menu1</li><li>▸ Menu1</li><li>▸ Menu1</li><li>▸ Menu1</li></ul>
  </div>
  <div class="footer-col contact-col" style="left:585px">
    <h4>Contact Us</h4>
    <ul>
      <li><svg width="9" height="10"><path d="M1 1l2.5 0 1 2.5-1.3 1c.5 1.2 1.2 1.9 2.3 2.3l1-1.3 2.5 1v2.5C4 9 1 6 1 1z" fill="#888"/></svg>+1800-555-0142</li>
      <li><svg width="10" height="8"><rect width="10" height="8" fill="#888"/><path d="M0 0l5 4 5-4" stroke="#3b3b3b" fill="none"/></svg>info@wadiqutub.net</li>
      <li style="align-items:flex-start;height:auto;line-height:19px"><svg width="8" height="11" style="margin-top:4px"><path d="M4 11C1 7 0 5.5 0 4a4 4 0 018 0c0 1.5-1 3-4 7z" fill="#888"/><circle cx="4" cy="4" r="1.5" fill="#3b3b3b"/></svg><span>Your Address, Your Country<br>Your Zip Code</span></li>
    </ul>
  </div>
  <div class="footer-col" style="left:758px">
    <h4>Social</h4>
    <div class="socials">
      <span role="img" aria-label="Social profile link" style="background:#3b5a9a"></span>
      <span role="img" aria-label="Social profile link" style="background:#2fa9e0"></span>
      <span role="img" aria-label="Social profile link" style="background:#1d6fa5"></span>
      <span role="img" aria-label="Social profile link" style="background:#d23a2b"></span>
    </div>
  </div>
  <div class="footer-bottom">
    <span class="copy">Copyright 2014 © Wadi Ibn Qutub - All Rights Reserved</span>
    <span class="legal">Site Map &nbsp; • &nbsp; Privacy Policy</span>
  </div>
</footer>

</body>
</html>
```